Design A HVAC Business Website with Figma

We are launching a Web Design Service for HVAC and other Home Improvement businesses. We need to create some demo sites. These sites will be used to develop Webflow templates, so they must look very professional and real.

I am providing some sample data for this design. **,DO NOT USE LOREM IPSUM** anywhere in this design. We will be featuring these designs on our website and marketing materials.

More information can be found on this Notion page https://pallid-cove-q29.wikinest.example/Web-Design-Project-7d2a9e1f04b8c365a1e9d70f42c6b8e3

Industry/Entity Type

HVAC, Plumbing, Remodeling, General Contractor

Number of Pages Required

5+ page

Requirements
Must have
• Must be professional

```html
<!DOCTYPE html>
<html lang="en">
<head>
<meta charset="utf-8">
<title>Harbor Crest HVAC</title>
<link href="https://fonts.googleapis.com/css2?family=Roboto:wght@400;500;700;900&display=swap" rel="stylesheet">
<style>
:root{
  --blue:#1b3f9c;
  --blue-dark:#173690;
  --red:#b80f0f;
  --ink:#111111;
  --muted:#555555;
  --field:#efefef;
  --white:#ffffff;
}
*{box-sizing:border-box;margin:0;padding:0}
html,body{width:1200px;height:3464px;overflow:hidden}
body{position:relative;font-family:'Roboto',sans-serif;color:var(--ink);background:var(--white)}
.abs{position:absolute}
section,header,footer,nav{position:absolute;left:0;width:1200px}

.topbar{top:0;height:50px;background:var(--blue-dark);color:var(--white);font-size:13px;font-weight:500}
.topbar .tagline{left:102px;top:17px;white-space:nowrap}
.topbar .avail{right:98px;top:15px;display:flex;align-items:center;gap:14px;white-space:nowrap}

.nav{top:50px;height:60px;background:var(--white)}
.brand{left:102px;top:17px;font-size:22px;font-weight:700;color:var(--red);white-space:nowrap}
.nav-links{left:495px;top:22px;width:460px;height:20px;font-size:14px;font-weight:500}
.nav-links span{position:absolute;top:0;white-space:nowrap}
.nav-links .active{color:var(--red)}
.quote-btn{left:964px;top:9px;width:138px;height:41px;background:var(--red);color:var(--white);font-size:14px;font-weight:500;display:flex;align-items:center;justify-content:center}

.hero{top:110px;height:547px;background:linear-gradient(90deg,#f1e7db 0%,#ede1d1 45%,#d9c6ad 100%);overflow:hidden}
.hero-photo{left:600px;top:0;width:600px;height:547px;background:linear-gradient(180deg,#d8c3a6 0%,#c9b090 40%,#2f4f86 70%,#24427a 100%);opacity:.9}
.hero .welcome{left:102px;top:55px;font-size:40px;font-weight:500}
.hero .title{left:102px;top:104px;font-size:56px;font-weight:700;color:var(--blue);white-space:nowrap}
.hero .sub{left:102px;top:183px;width:520px;font-size:17.5px;line-height:21px}
.form{left:102px;top:246px;width:423px;height:273px;background:var(--white)}
.form h3{position:absolute;left:31px;top:18px;font-size:17px;font-weight:500}
.field{position:absolute;left:31px;width:362px;background:var(--field);font-size:12.5px;padding:10px 17px;color:#222}
.submit{position:absolute;left:31px;top:215px;width:137px;height:40px;background:var(--red);color:var(--white);font-weight:700;font-size:17px;display:flex;align-items:center;justify-content:center}
.help{position:absolute;left:205px;top:220px;display:flex;gap:12px;align-items:center}
.help small{display:block;font-size:10px;font-weight:500}
.help strong{font-size:18px;font-weight:500}

.about{top:657px;height:621px;background:var(--white)}
.about-img1{left:116px;top:49px;width:468px;height:366px;background:linear-gradient(135deg,#8a8a8a,#d7d3ce 55%,#5a5a5a)}
.about-img2{left:231px;top:294px;width:407px;height:273px;background:linear-gradient(135deg,#f0f0f0,#9aa7c2 50%,#2c4a8c);border:7px solid var(--white)}
.about h2{left:730px;top:92px;font-size:40px;font-weight:700}
.about .copy{left:730px;top:166px;width:440px;font-size:15.5px;line-height:22px}
.about .copy p+p{margin-top:22px}
.btn-red{left:730px;top:407px;width:144px;height:47px;background:var(--red);color:var(--white);font-size:17px;font-weight:500;display:flex;align-items:center;justify-content:center}

.services{top:1278px;height:441px;background:var(--blue)}
.section-title{left:0;width:1200px;text-align:center;font-size:40px;font-weight:700}
.services .section-title{top:32px;color:var(--white)}
.card{top:98px;width:244px;height:293px;background:var(--white);text-align:center}
.card .photo{height:157px;width:244px}
.card .badge{position:absolute;left:95px;top:128px;width:54px;height:54px;border-radius:50%;background:var(--white);display:flex;align-items:center;justify-content:center}
.card h4{position:absolute;left:0;top:196px;width:244px;font-size:13px;font-weight:700}
.card p{position:absolute;top:220px;left:20px;width:204px;font-size:8.5px;line-height:12px;color:var(--muted)}

.why{top:1719px;height:601px;background:linear-gradient(180deg,#ffffff 0%,#f4f4f6 35%,#d6d9df 100%)}
.why .section-title{top:37px}
.worker{left:484px;top:103px;width:256px;height:498px;background:linear-gradient(180deg,#e9e9ef 0%,#2d55c0 25%,#2248b5 70%,#b8864a 85%,#2248b5 100%);border-radius:110px 110px 0 0}
.perk{font-size:17px;font-weight:700;line-height:22px;white-space:nowrap}
.perk-icon{width:84px;height:84px;border-radius:50%;background:var(--red);border:4px solid var(--blue);display:flex;align-items:center;justify-content:center}

.testimonials{top:2320px;height:424px;background:radial-gradient(ellipse at center,#2650b5 0%,#1b3f9c 70%)}
.testimonials .section-title{top:37px;color:var(--white)}
.review{top:120px;width:340px;text-align:center;color:var(--white)}
.avatar{width:78px;height:78px;border-radius:50%;margin:0 auto;background:linear-gradient(180deg,#cfd6e4,#6f7a93);border:3px solid var(--white)}
.review h5{margin-top:13px;font-size:22px;font-weight:500}
.stars{margin-top:10px;display:flex;justify-content:center;gap:8px}
.review p{margin-top:18px;font-size:12.5px;line-height:19px}
.arrow{top:2511px;width:48px;height:48px;border:2px solid var(--white);border-radius:50%;display:flex;align-items:center;justify-content:center}

.contact{top:2744px;height:504px;background:var(--white)}
.contact h2{left:79px;top:35px;font-size:40px;font-weight:700}
.input{left:79px;width:493px;border:1px solid #9a9a9a;font-size:15px;color:#777;padding:16px 27px}
.send{left:79px;top:395px;width:493px;height:53px;background:var(--blue);color:var(--white);font-size:23px;font-weight:500;display:flex;align-items:center;justify-content:center}
.map{left:625px;top:2px;width:575px;height:446px;background:linear-gradient(135deg,#eef0f3,#e2e5ea)}

.footer{top:3248px;height:216px;background:var(--blue);color:var(--white)}
.footer .fbrand{left:79px;top:44px;font-size:18px;font-weight:700}
.social{top:84px;width:34px;height:34px;border:2px solid var(--white);border-radius:50%}
.footer .copy{left:77px;top:148px;font-size:13px;font-weight:500}
.flinks{left:312px;top:43px;font-size:13px;line-height:21.5px}
.faddr{left:460px;top:43px;width:250px;font-size:13px;line-height:21px}
.footer h6{left:776px;top:45px;font-size:24px;font-weight:500;white-space:nowrap}
.news-input{left:776px;top:89px;width:194px;height:44px;border:1px solid #9fb0da;font-size:13px;color:#c8d2ec;padding:13px 12px}
.news-btn{left:970px;top:89px;width:137px;height:44px;background:var(--white);color:var(--blue);font-size:16px;font-weight:700;display:flex;align-items:center;justify-content:center}
</style>
</head>
<body>

<header class="topbar">
  <div class="abs tagline">Servicing the Heating, Ventilation, and Air Conditioning for Over 13 Years!</div>
  <div class="abs avail">
    <svg width="20" height="20" viewBox="0 0 20 20" aria-hidden="true"><circle cx="10" cy="10" r="10" fill="#fff"/><path d="M7 5.5l2 2-1 1.3c.6 1.3 1.6 2.3 2.9 2.9l1.3-1 2 2-1.2 1.5C9.8 14 6 10.2 5.8 6.7z" fill="#173690"/></svg>
    <span>We Are Available 24/7 : 1-555-014-2287</span>
  </div>
</header>

<nav class="nav">
  <div class="abs brand">Harbor Crest HVAC</div>
  <div class="abs nav-links">
    <span class="active" style="left:0">Home</span>
    <span style="left:54px">About Us</span>
    <span style="left:126px">Services</span>
    <span style="left:196px">Products</span>
    <span style="left:273px">Gallery</span>
    <span style="left:332px">Contact Us</span>
    <span style="left:417px">Blog</span>
  </div>
  <div class="abs quote-btn">Get A Quote</div>
</nav>

<section class="hero">
  <div class="abs hero-photo" role="img" aria-label="Smiling HVAC technician in a blue uniform and cap holding a clipboard"></div>
  <div class="abs welcome">Welcome To</div>
  <div class="abs title">HARBOR CREST HVAC</div>
  <div class="abs sub">Your trusted source for heating, ventilation, and air conditioning services in San Diego County.</div>
  <div class="abs form">
    <h3>REQUEST SERVICE</h3>
    <div class="field" style="top:51px;height:34px">Name</div>
    <div class="field" style="top:97px;height:35px">Email or Phone</div>
    <div class="field" style="top:144px;height:59px">How Can We Help You ?</div>
    <div class="submit">SUBMIT</div>
    <div class="help">
      <svg width="34" height="34" viewBox="0 0 34 34" aria-hidden="true"><circle cx="17" cy="17" r="16" fill="none" stroke="#b80f0f" stroke-width="1.5"/><path d="M11 9l3.5 3.5-1.6 2c1 2.3 2.8 4.1 5.1 5.1l2-1.6L23.5 21.5 21.6 24C15 23.6 10.4 19 10 12.4z" fill="none" stroke="#b80f0f" stroke-width="1.5"/></svg>
      <div><small>NEED HELP? CALL US !</small><strong>1-555-014-2287</strong></div>
    </div>
  </div>
</section>

<section class="about">
  <div class="abs about-img1" role="img" aria-label="Technician in a hard hat repairing pipes under an indoor unit"></div>
  <div class="abs about-img2" role="img" aria-label="Technician in a yellow hard hat servicing an outdoor air conditioner"></div>
  <h2 class="abs">ABOUT US</h2>
  <div class="abs copy">
    <p>Our team of certified technicians has been providing top-notch service to our customers for over 13 years.</p>
    <p>At Harbor Crest HVAC, we believe in providing personalized service that meets the unique needs of our customers. We know that HVAC problems can be stressful and disruptive to your daily routine, which is why we offer flexible scheduling and 24/7 emergency services to ensure that we are always available when you need us.</p>
  </div>
  <div class="abs btn-red">Learn More</div>
</section>

<section class="services">
  <h2 class="abs section-title">OUR SERVICE</h2>
  <div class="abs card" style="left:79px">
    <div class="photo" role="img" aria-label="Technician working on a furnace" style="background:linear-gradient(135deg,#8b3a2a,#c9b8a2 50%,#2a4e9a)"></div>
    <div class="badge"><svg width="30" height="24" viewBox="0 0 30 24" aria-hidden="true" fill="none" stroke="#1b3f9c" stroke-width="1.5"><rect x="2" y="3" width="26" height="10" rx="2"/><path d="M6 9h18M8 16v5M15 16v5M22 16v5"/></svg></div>
    <h4>HEATING SERVICES</h4>
    <p>Whether you need a new furnace installed, an old system repaired, or routine maintenance, our team has the expertise to keep you warm and cozy all winter long.</p>
  </div>
  <div class="abs card" style="left:345px">
    <div class="photo" role="img" aria-label="Technician in a hard hat installing an indoor air conditioner" style="background:linear-gradient(180deg,#eceff3,#9fb0cc 55%,#2f64c4)"></div>
    <div class="badge"><svg width="28" height="28" viewBox="0 0 28 28" aria-hidden="true" fill="none" stroke="#1b3f9c" stroke-width="1.5"><circle cx="10" cy="8" r="4"/><path d="M3 25v-5a7 7 0 0 1 14 0v5z"/><rect x="17" y="15" width="9" height="9"/><circle cx="21.5" cy="19.5" r="2"/></svg></div>
    <h4>AIR CONDITIONING SERVICES</h4>
    <p>Stay cool and comfortable all summer long with our expert air conditioning services. We offer installation, repair, and maintenance services for all types of AC units.</p>
  </div>
  <div class="abs card" style="left:611px">
    <div class="photo" role="img" aria-label="Person relaxing on the floor beside an air purifier" style="background:linear-gradient(135deg,#6a625a,#d9d6d1 50%,#8a8580)"></div>
    <div class="badge"><svg width="28" height="28" viewBox="0 0 28 28" aria-hidden="true" fill="none" stroke="#1b3f9c" stroke-width="1.5"><path d="M3 13L14 4l11 9M6 11v13h16V11"/><path d="M10 16h8M10 20h8"/></svg></div>
    <h4>INDOOR AIR QUALITY</h4>
    <p>We know that indoor air quality is essential for your health and comfort. Our team can help you improve your indoor air quality by installing air purifiers, humidifiers, and ventilation systems.</p>
  </div>
  <div class="abs card" style="left:877px">
    <div class="photo" role="img" aria-label="Technician with a drill mounting a commercial outdoor unit" style="background:linear-gradient(135deg,#bfb3a3,#e7e4df 50%,#3a5ea8)"></div>
    <div class="badge"><svg width="30" height="26" viewBox="0 0 30 26" aria-hidden="true" fill="none" stroke="#1b3f9c" stroke-width="1.5"><rect x="2" y="2" width="26" height="10" rx="2"/><path d="M6 7h18"/><circle cx="15" cy="19" r="5"/><path d="M15 14v10M10 19h10"/></svg></div>
    <h4>COMMERCIAL HVAC</h4>
    <p>Our commercial HVAC services are designed to keep your business running smoothly. From routine maintenance to complex installations, our team can handle it all.</p>
  </div>
</section>

<section class="why">
  <h2 class="abs section-title">WHY CHOOSE HARBOR CREST?</h2>
  <div class="abs worker" role="img" aria-label="Bearded HVAC technician in blue overalls and tool belt giving a thumbs up"></div>

  <div class="abs perk-icon" style="left:134px;top:176px"><svg width="40" height="40" viewBox="0 0 40 40" aria-hidden="true" fill="none" stroke="#fff" stroke-width="2"><circle cx="20" cy="20" r="16"/><circle cx="20" cy="16" r="5"/><path d="M11 30a9 9 0 0 1 18 0"/></svg></div>
  <div class="abs perk" style="left:245px;top:197px">Experienced and certified<br>technicians</div>
  <div class="abs perk-icon" style="left:134px;top:290px"><svg width="40" height="40" viewBox="0 0 40 40" aria-hidden="true" fill="none" stroke="#fff" stroke-width="2"><circle cx="20" cy="20" r="16"/><text x="20" y="24" fill="#fff" stroke="none" font-size="11" font-family="Roboto,sans-serif" text-anchor="middle">24</text></svg></div>
  <div class="abs perk" style="left:245px;top:321px">24/7 emergency services</div>
  <div class="abs perk-icon" style="left:134px;top:407px"><svg width="40" height="40" viewBox="0 0 40 40" aria-hidden="true" fill="none" stroke="#fff" stroke-width="2"><circle cx="20" cy="20" r="15"/><path d="M20 11v9l6 4"/></svg></div>
  <div class="abs perk" style="left:245px;top:438px">Flexible scheduling</div>

  <div class="abs perk-icon" style="left:984px;top:142px"><svg width="40" height="40" viewBox="0 0 40 40" aria-hidden="true" fill="none" stroke="#fff" stroke-width="2"><circle cx="20" cy="20" r="15"/><text x="20" y="26" fill="#fff" stroke="none" font-size="17" font-family="Roboto,sans-serif" text-anchor="middle">$</text></svg></div>
  <div class="abs perk" style="right:245px;top:173px;text-align:right">Upfront pricing</div>
  <div class="abs perk-icon" style="left:984px;top:252px"><svg width="40" height="40" viewBox="0 0 40 40" aria-hidden="true" fill="none" stroke="#fff" stroke-width="2"><circle cx="20" cy="17" r="11"/><path d="M15 17l4 4 7-7M14 27l-3 9 9-4 9 4-3-9"/></svg></div>
  <div class="abs perk" style="right:245px;top:272px;text-align:right">High-quality<br>equipment and parts</div>
  <div class="abs perk-icon" style="left:984px;top:365px"><svg width="40" height="40" viewBox="0 0 40 40" aria-hidden="true" fill="none" stroke="#fff" stroke-width="2"><circle cx="20" cy="20" r="15"/><circle cx="20" cy="16" r="4"/><path d="M13 27a7 7 0 0 1 14 0"/></svg></div>
  <div class="abs perk" style="right:245px;top:396px;text-align:right">Personalized service</div>
  <div class="abs perk-icon" style="left:984px;top:478px"><svg width="40" height="40" viewBox="0 0 40 40" aria-hidden="true" fill="none" stroke="#fff" stroke-width="2"><circle cx="22" cy="15" r="8"/><path d="M18 15l3 3 5-5M6 32h8l8 3 12-7"/></svg></div>
  <div class="abs perk" style="right:245px;top:509px;text-align:right">Satisfaction Guarantee</div>
</section>

<section class="testimonials">
  <h2 class="abs section-title">TESTIMONIALS</h2>
  <div class="abs review" style="left:193px">
    <div class="avatar" role="img" aria-label="Portrait of reviewer Marcus Hale"></div>
    <h5>MARCUS HALE</h5>
    <div class="stars">
      <svg width="30" height="29" viewBox="0 0 24 23" aria-hidden="true"><path d="M12 0l3.6 7.3 8 1.2-5.8 5.6 1.4 8L12 18.3 4.8 22.1l1.4-8L.4 8.5l8-1.2z" fill="#f7b500"/></svg>
      <svg width="30" height="29" viewBox="0 0 24 23" aria-hidden="true"><path d="M12 0l3.6 7.3 8 1.2-5.8 5.6 1.4 8L12 18.3 4.8 22.1l1.4-8L.4 8.5l8-1.2z" fill="#f7b500"/></svg>
      <svg width="30" height="29" viewBox="0 0 24 23" aria-hidden="true"><path d="M12 0l3.6 7.3 8 1.2-5.8 5.6 1.4 8L12 18.3 4.8 22.1l1.4-8L.4 8.5l8-1.2z" fill="#f7b500"/></svg>
      <svg width="30" height="29" viewBox="0 0 24 23" aria-hidden="true"><path d="M12 0l3.6 7.3 8 1.2-5.8 5.6 1.4 8L12 18.3 4.8 22.1l1.4-8L.4 8.5l8-1.2z" fill="#f7b500"/></svg>
      <svg width="30" height="29" viewBox="0 0 24 23" aria-hidden="true"><path d="M12 0l3.6 7.3 8 1.2-5.8 5.6 1.4 8L12 18.3 4.8 22.1l1.4-8L.4 8.5l8-1.2z" fill="#f7b500"/></svg>
    </div>
    <p>Next day service in the middle of the Las Vegas summer, you guys rock!! I am not one for reviews but when I get service like this it is motivating for me to share with the world. Best I have seen for Las Vegas AC Repair. Thanks guys.</p>
  </div>
  <div class="abs review" style="left:689px">
    <div class="avatar" role="img" aria-label="Portrait of reviewer Dana Whitfield"></div>
    <h5>DANA WHITFIELD</h5>
    <div class="stars">
      <svg width="30" height="29" viewBox="0 0 24 23" aria-hidden="true"><path d="M12 0l3.6 7.3 8 1.2-5.8 5.6 1.4 8L12 18.3 4.8 22.1l1.4-8L.4 8.5l8-1.2z" fill="#f7b500"/></svg>
      <svg width="30" height="29" viewBox="0 0 24 23" aria-hidden="true"><path d="M12 0l3.6 7.3 8 1.2-5.8 5.6 1.4 8L12 18.3 4.8 22.1l1.4-8L.4 8.5l8-1.2z" fill="#f7b500"/></svg>
      <svg width="30" height="29" viewBox="0 0 24 23" aria-hidden="true"><path d="M12 0l3.6 7.3 8 1.2-5.8 5.6 1.4 8L12 18.3 4.8 22.1l1.4-8L.4 8.5l8-1.2z" fill="#f7b500"/></svg>
      <svg width="30" height="29" viewBox="0 0 24 23" aria-hidden="true"><path d="M12 0l3.6 7.3 8 1.2-5.8 5.6 1.4 8L12 18.3 4.8 22.1l1.4-8L.4 8.5l8-1.2z" fill="#f7b500"/></svg>
      <svg width="30" height="29" viewBox="0 0 24 23" aria-hidden="true"><path d="M12 0l3.6 7.3 8 1.2-5.8 5.6 1.4 8L12 18.3 4.8 22.1l1.4-8L.4 8.5l8-1.2z" fill="#f7b500"/></svg>
    </div>
    <p>Next day service in the middle of the Las Vegas summer, you guys rock!! I am not one for reviews but when I get service like this it is motivating for me to share with the world. Best I have seen for Las Vegas AC Repair. Thanks guys.</p>
  </div>
</section>
<div class="abs arrow" style="left:70px"><svg width="14" height="20" viewBox="0 0 14 20" aria-hidden="true"><path d="M10 3L3 10l7 7" fill="none" stroke="#fff" stroke-width="2"/></svg></div>
<div class="abs arrow" style="left:1082px"><svg width="14" height="20" viewBox="0 0 14 20" aria-hidden="true"><path d="M4 3l7 7-7 7" fill="none" stroke="#fff" stroke-width="2"/></svg></div>

<section class="contact">
  <h2 class="abs">CONTACT US</h2>
  <div class="abs input" style="top:103px;height:54px">Enter your name</div>
  <div class="abs input" style="top:173px;height:54px">Enter your email</div>
  <div class="abs input" style="top:243px;height:135px">Message</div>
  <div class="abs send">Submit</div>
  <div class="abs map" role="img" aria-label="Street map showing the office location"></div>
</section>

<footer class="footer">
  <div class="abs fbrand">Harbor Crest HVAC</div>
  <div class="abs social" style="left:79px" aria-label="Social profile"></div>
  <div class="abs social" style="left:122px" aria-label="Social profile"></div>
  <div class="abs social" style="left:165px" aria-label="Social profile"></div>
  <div class="abs social" style="left:208px" aria-label="Social profile"></div>
  <div class="abs copy">©2023 Harbor Crest HVAC</div>
  <div class="abs flinks">Home<br>About us<br>Service<br>Testimonial<br>FAQ<br>Why choose us<br>Contact us</div>
  <div class="abs faddr">Crestline Heating and Air Mr. Tomas Alvero 412 Marlow Point, Suite 208, Springvale, IN 46000<br>1-555-014-2287<br>info@crestlineheating.example<br>www.crestlineheating.example</div>
  <h6 class="abs">Subscribe To Our Newsletter</h6>
  <div class="abs news-input">Enter your email</div>
  <div class="abs news-btn">Subscribe</div>
</footer>

</body>
</html>
```